Salon Signage

We need a new company sign designed for the exterior of our salon. I have attached our current logos for an idea. I have also attached a photo of what salon looks like currently.

```html
<!DOCTYPE html>
<html lang="en">
<head>
<meta charset="utf-8">
<title>SilkShine Beauty Salon – Exterior Sign Options</title>
<link rel="stylesheet" href="https://fonts.googleapis.com/css2?family=Archivo+Black&family=Allura&display=swap">
<style>
  :root {
    --page-bg: #eceeed;
    --divider: #ffffff;
    --frame: #b3b3b3;
    --shadow: rgba(0, 0, 0, 0.35);
    --ink: #0d0d0d;
    --blush: #f6e3e1;
    --blush-edge: #ecd2cf;
    --magenta: #a0238b;
    --hair-light: #ebe2b4;
    --hair-mid: #d6c78d;
    --hair-dark: #bfa969;
  }
  html, body {
    margin: 0;
    padding: 0;
    width: 1200px;
    height: 1044px;
    overflow: hidden;
    background: var(--page-bg);
  }
  .canvas {
    position: relative;
    width: 1200px;
    height: 1044px;
  }
  .divider {
    position: absolute;
    left: 0;
    top: 514px;
    width: 1200px;
    height: 15px;
    background: var(--divider);
  }
  .sign {
    position: absolute;
    display: block;
  }
  .sign--circle-mark { left: 0; top: 0; }
  .sign--open-mark { left: 0; top: 520px; }
  .wordmark {
    font-family: "Archivo Black", "Arial Black", sans-serif;
    fill: var(--ink);
  }
  .tagline {
    font-family: "Allura", cursive;
    fill: var(--ink);
  }
</style>
</head>
<body>
<main class="canvas">

  <svg class="sign sign--circle-mark" width="1200" height="514" viewBox="0 0 1200 514" aria-label="Sign option one: SilkShine Beauty Salon">
    <defs>
      <linearGradient id="hairTone" x1="0" y1="0" x2="1" y2="1">
        <stop offset="0" stop-color="var(--hair-mid)"/>
        <stop offset="0.35" stop-color="var(--hair-light)"/>
        <stop offset="0.7" stop-color="var(--hair-mid)"/>
        <stop offset="1" stop-color="var(--hair-dark)"/>
      </linearGradient>
      <radialGradient id="portraitTone" cx="0.5" cy="0.45" r="0.6">
        <stop offset="0" stop-color="#7a5a4e"/>
        <stop offset="0.6" stop-color="#c9a59e"/>
        <stop offset="1" stop-color="#f3dcd8"/>
      </radialGradient>
      <filter id="signShadow" x="-5%" y="-10%" width="115%" height="140%">
        <feDropShadow dx="10" dy="12" stdDeviation="4" flood-color="var(--shadow)"/>
      </filter>
    </defs>
    <rect class="sign-frame" x="76" y="137" width="1047" height="225" fill="var(--frame)" filter="url(#signShadow)"/>
    <rect class="sign-face" x="84" y="145" width="1032" height="209" fill="url(#hairTone)" role="img" aria-label="Photograph of smooth flowing blonde hair"/>
    <circle class="brand-circle" cx="207" cy="244" r="93" fill="var(--blush)" stroke="var(--blush-edge)" stroke-width="2"/>
    <text class="wordmark" x="327" y="237" font-size="100" textLength="555" lengthAdjust="spacingAndGlyphs">SILKSHINE</text>
    <text class="tagline" x="530" y="312" font-size="78" textLength="330" lengthAdjust="spacingAndGlyphs">Beauty Salon</text>
    <circle class="stylist-portrait" cx="984" cy="246" r="77" fill="url(#portraitTone)" role="img" aria-label="Illustration of a stylist holding hair dryer, brushes, scissors and colour swatches"/>
  </svg>

  <svg class="sign sign--open-mark" width="1200" height="524" viewBox="0 520 1200 524" aria-label="Sign option two: SilkShine Beauty Salon">
    <rect class="sign-frame" x="76" y="657" width="1047" height="241" fill="var(--frame)" filter="url(#signShadow)"/>
    <rect class="sign-face" x="84" y="665" width="1032" height="226" fill="url(#hairTone)" role="img" aria-label="Photograph of smooth flowing blonde hair"/>
    <circle class="brand-circle" cx="190" cy="780" r="90" fill="var(--magenta)"/>
    <text class="wordmark" x="282" y="774" font-size="108" textLength="591" lengthAdjust="spacingAndGlyphs">SILKSHINE</text>
    <text class="tagline" x="524" y="852" font-size="80" textLength="326" lengthAdjust="spacingAndGlyphs">Beauty Salon</text>
    <circle class="stylist-portrait" cx="984" cy="781" r="83" fill="url(#portraitTone)" role="img" aria-label="Illustration of a stylist holding hair dryer, brushes, scissors and colour swatches"/>
  </svg>

  <div class="divider"></div>
</main>
</body>
</html>
```